DORLIT HOMES Professional Home Buyers

Please see two files uploaded. One is my new LOGO (thanks Quenby) and the other gives the wording and pages desired. Of course I am open to suggestions to further enhance what I'm about. I don't want testimonials or houses to buy to appear but to have room for them when I'm ready. I am a real estate investor not a licensed real estate agent. For FAQ i want just the questions to appear and when they click on the question the answer appears and when they click on the question again the answer disappears. make sense? When you read my wording and my idea of pages you'll get an idea of what I'm about. Suggestions are welcomed.

Industry/Entity Type

Real Estate

Number of Pages Required

5+ page

Requirements
Must have
• FAQ pages only questions appear. They click on question the answer appears underneath. they click on question again, the answer disappears. Also, I of course, want my new LOGO to appear on each page I don't know if it will look better all by itself or blended in somehow? Call now 418-555-0193 on each page also. I will get a real phone number before website goes live. If you have a better way of wording what I'm describing please let me know, I am open to feedback
Nice to have
• Anything that the average homeowner can relate to (yea I know, that doesn't help you much, right?)
• Testimonial page and houses to buy page could be done with just the shell ready in the wings for when my business grows it will be ready all that it would need then are the wording and pictures to be uploaded onto the website page. make sense?
Should not have
• I don't want it too elegant or rich looking as I believe my audience will be mostly the average homeowner who needs help

```html
<!DOCTYPE html>
<html lang="en">
<head>
<meta charset="utf-8">
<title>DORLIT HOMES – We Buy Houses As Is</title>
<link rel="stylesheet" href="https://fonts.googleapis.com/css2?family=Montserrat:wght@400;600;700&family=Open+Sans:wght@400;600&display=swap">
<style>
  :root{
    --blue:#2c6fc6;
    --blue-dark:#1d55a3;
    --navy:#0f2a5c;
    --navy-deep:#0a1f47;
    --ink:#1f3566;
    --text:#5c6270;
    --pill:#eceef1;
    --footer:#1d2433;
    --footer-text:#8a91a0;
    --white:#ffffff;
  }
  *{margin:0;padding:0;box-sizing:border-box}
  html,body{width:1200px;height:2372px;overflow:hidden;background:var(--white)}
  body{position:relative;font-family:"Open Sans",Arial,sans-serif;color:var(--text)}
  .abs{position:absolute}
  .heading{font-family:"Montserrat",Arial,sans-serif;font-weight:700;color:var(--ink);text-align:center;letter-spacing:1px}
  .btn{position:absolute;display:flex;align-items:center;justify-content:center;gap:14px;background:var(--blue);color:var(--white);font-family:"Montserrat",Arial,sans-serif;font-weight:600;font-size:17px;letter-spacing:3px;border-radius:3px}

  /* hero */
  .hero{left:0;top:0;width:1200px;height:610px;background:linear-gradient(180deg,#c9d6e3 0%,#dfe6ec 40%,#b8ad93 70%,#5f7048 100%)}
  .hero-photo{position:absolute;inset:0;background:linear-gradient(180deg,rgba(160,185,210,.5) 0%,rgba(220,210,185,.4) 55%,rgba(70,95,60,.7) 100%)}
  .brand{left:80px;top:36px;display:flex;align-items:center;gap:12px;font-family:"Montserrat",Arial,sans-serif;font-weight:700;font-size:26px;color:var(--navy)}
  .brand-mark{width:26px;height:26px;background:var(--navy)}
  .phone{right:70px;top:24px;display:flex;align-items:center;gap:10px;font-family:"Montserrat",Arial,sans-serif;font-size:17px;color:var(--navy);font-weight:600}
  .nav{left:500px;top:64px;display:flex;gap:38px;font-family:"Montserrat",Arial,sans-serif;font-size:14px;font-weight:600;color:var(--navy);letter-spacing:1px}
  .hero-card{left:480px;top:400px;width:340px;height:160px;background:rgba(18,60,130,.9);color:var(--white);text-align:center;padding-top:22px;font-family:"Montserrat",Arial,sans-serif}
  .hero-card h1{font-size:32px;font-weight:700;letter-spacing:1px}
  .hero-card p{font-size:22px;line-height:1.3;margin-top:8px}
  .hero-card strong{font-weight:700;font-size:24px}

  /* intro */
  .intro-title{left:0;top:692px;width:1200px;font-size:27px}
  .intro-text{left:170px;top:780px;width:860px;font-size:15px;line-height:1.9;text-align:center}

  /* cash band */
  .cash{left:0;top:1024px;width:1200px;height:688px;background:linear-gradient(135deg,var(--navy) 0%,var(--navy-deep) 55%,#143572 100%)}
  .cash-title{top:86px;left:0;width:1200px;color:var(--white);font-size:27px}
  .cash-photo{left:352px;top:136px;width:496px;height:280px;border:4px solid var(--white);background:linear-gradient(180deg,#a9c3dc 0%,#e3d7b0 55%,#6f8a4e 100%)}
  .cash-text{left:250px;top:436px;width:700px;color:#dfe6f2;font-size:15px;line-height:1.9;text-align:center}

  /* benefits */
  .sell-title{left:0;top:1788px;width:1200px;font-size:27px}
  .pill{position:absolute;height:48px;background:var(--pill);border-radius:3px;display:flex;align-items:center;justify-content:center;font-family:"Montserrat",Arial,sans-serif;font-size:14px;font-weight:600;color:#6a7180;letter-spacing:1px}

  /* footer */
  .footer{left:0;top:2088px;width:1200px;height:284px;background:var(--footer)}
  .social{position:absolute;top:72px;width:50px;height:50px}
  .footer-nav{top:158px;left:0;width:1200px;display:flex;justify-content:center;gap:40px;font-family:"Montserrat",Arial,sans-serif;font-size:13px;letter-spacing:1px;color:var(--footer-text)}
  .copyright{top:204px;left:0;width:1200px;text-align:center;font-size:13px;color:var(--footer-text)}
  .copyright b{color:var(--white)}
</style>
</head>
<body>

<section class="abs hero">
  <div class="hero-photo" role="img" aria-label="Two-storey suburban family house with gabled roof, front lawn and trees under a soft sky"></div>
  <div class="abs brand"><span class="brand-mark"></span>DORLIT HOMES</div>
  <div class="abs phone">
    <svg width="18" height="18" viewBox="0 0 24 24"><path d="M6.6 10.8a15 15 0 0 0 6.6 6.6l2.2-2.2a1 1 0 0 1 1-.25 11 11 0 0 0 3.6.6 1 1 0 0 1 1 1V20a1 1 0 0 1-1 1A17 17 0 0 1 3 4a1 1 0 0 1 1-1h3.5a1 1 0 0 1 1 1 11 11 0 0 0 .6 3.6 1 1 0 0 1-.25 1z" fill="#0f2a5c"/></svg>
    418-555-0193
  </div>
  <nav class="abs nav"><span>HOME</span><span>ABOUT US</span><span>FAQ</span><span>CONTACT US</span><span>TESTIMONIALS</span><span>HOUSES TO BUY</span></nav>
  <div class="abs hero-card">
    <h1>DORLIT HOMES</h1>
    <p>WILL BUY YOUR HOUSE AS IS<br><strong>FAST AND HASSLE</strong></p>
  </div>
  <div class="btn" style="left:500px;top:572px;width:200px;height:58px">LEARN MORE
    <svg width="18" height="12" viewBox="0 0 18 12"><path d="M0 6h15M10 1l5 5-5 5" stroke="#fff" stroke-width="2" fill="none"/></svg>
  </div>
</section>

<h2 class="abs heading intro-title">WE BUY HOUSES IN ANY CONDITION!</h2>
<p class="abs intro-text">Don't waste another penny on expensive repairs! DORLIT HOMES is currently buying houses throughout Maryland. We buy houses "as-is", we pay cash, we handle all traditional closing costs and we can close in as quickly as a week. Contact us today for your free, no obligation quote.</p>
<div class="btn" style="left:432px;top:888px;width:336px;height:56px">GET YOUR FREE QUOTE</div>

<section class="abs cash">
  <h2 class="abs heading cash-title">GET CASH FOR YOUR HOUSE!</h2>
  <div class="abs cash-photo" role="img" aria-label="Large yellow two-storey house with white porch and green lawn"></div>
  <p class="abs cash-text">DORLIT HOMES has real estate investors ready to buy your house in as little as seven days. We buy houses, townhomes, condos, duplexes and multi-tenant buildings from owners looking to sell quickly!</p>
  <div class="btn" style="left:480px;top:524px;width:240px;height:56px">GET MORE INFO</div>
</section>

<h2 class="abs heading sell-title">SELL YOUR HOME FAST!</h2>
<div class="pill" style="left:172px;top:1880px;width:240px">WE PAY ALL CASH</div>
<div class="pill" style="left:440px;top:1880px;width:312px">WE PAY MOST CLOSING COSTS</div>
<div class="pill" style="left:792px;top:1880px;width:236px">WE BUY "AS IS"</div>
<div class="pill" style="left:172px;top:1952px;width:488px">NO WAITING FOR BANK LOAN APPROVALS</div>
<div class="pill" style="left:700px;top:1952px;width:232px">QUICK CLOSINGS</div>

<footer class="abs footer">
  <span class="social" style="left:492px;background:#3b5a9a"></span>
  <span class="social" style="left:546px;background:#2aa3e0"></span>
  <span class="social" style="left:600px;background:#d63a2f"></span>
  <span class="social" style="left:654px;background:#1f78b4"></span>
  <nav class="abs footer-nav"><span>HOME</span><span>ABOUT US</span><span>FAQ</span><span>CONTACT US</span><span>TESTIMONIALS</span><span>HOUSES TO BUY</span></nav>
  <p class="abs copyright">© 2015 <b>DORLIT HOMES</b> · All Rights Reserved</p>
</footer>

</body>
</html>
```